Guarenteed! - Homepage Website Design - Coding not required- Winner to complete further pages

Hi all,

We're looking at redesigning our current website with a few adjustments to other pages but the main adjustments will be on the homepage which is what this design request is for. Please note : any of these ideas can be changed if you have something particularly different / special in mind etc.

P.S Coding is not required, just a design.

- Our website -

Our website is simply a price comparison website that allows customers to find companies within their area at the best price. The products available are mostly related to the vehicle trade and all refer to vinyl. This includes the likes of vehicle window tint, vehicle colour change vehicle wrap, vehicle signage as well as other cosmetic vinyl modifications. We allow the customer to search for their product within their chosen area and receive a list of companies who supply their product within that area. From here they can compare prices and view further details on the company.

- What we're looking to do -

We're looking first of all to adjust how the website homepage is displayed, this includes adding images and adjusting the colours that are explained below:

First of all, we look to spread out each of the 12 products (which can be seen on the website as it stands) and add an image to each of the products (all being spaced out as shown in our sketch)

We've been told the website looks too busy so we're thinking if we adjust the colours to more simplier neutral colours as well as the main focus of the website being on the 12 images, that would be great.

- Logo + Banner -

Logo to remain top left although banner may be removed / adjusted to make simplier.

- Colours -

Adjustments - Colours shades
We want the website to still look exciting but simplify the colours. Needs to be kept up to date with the colours / textures etc (bright colours to highlight keypoints)
We're still looking to use either blue or orange or maybe both to highlight these keypoints but the main website to be light colours and maybe even black on white background. The entire homepage can be adjusted colour wise if you feel it fits into your theme including menu bars, banners etc. The key is to get this right with being not too overpowering with the colours but still look interesting and up to date.

- 1 - 4 steps banner - (text may change)

This sits just under the logo and explains to the user how easy the website is to use and the steps they need to take. This may change to a 1 - 5 steps but we're looking to have this designed once the overall colours / theme of the website is sorted.

- 12 images - 4 x 3

This is the main focus of the website and will be the main focus of what the customer sees first of all. This will be where they select their product and then underneath, enter their postcode and distance they would like to search within. As explained further up, we have some of the product images available so if you can where possible add these to the design and then duplicate the images on those we currently don't have available.

- 12 Images -Titles -

These titles will be in this order from left to right and etc

- Colour Change Wrap
- Printed Vehicle Wrap
- Window Tint
- Headlight Tint
- Vehicle Signage
- Shop Signage
- Roof Vinyl Wrap
- Bonnet Vinyl Wrap
- Carbon Fibre Vinyl
- Stickerbomb Vinyl
- Clear Protective Vinyl
- Wheel Refurb

Text to be quite large, centered and with the o to the left of the title. Short titles like 'Window Tint' should fit on one line in the middle of the box where as titles such as ' Stickerbomb Vinyl Wrap' should have the 'Stickerbomb Vinyl' on the first line with the 'Wrap' on the line below. The background of this text is up to experient, might be worth just a simple colour or it might be worth using a bright blue or orange to keep in with the theme of the logo etc.

These will also have the circle tick box to the left of the title (as on the current website) where the customer clicks to select the product they have available.
We were also thinking that if when the customer ticks the circle on their selected box, the box is highlighted in some way to show this.

- Search Block -

This will appear under the 12 images and allows the customer to input their postcode and distance for the search criteria. Colours on this can of course be adjusted to keep in theme with the website.

- Under the 12 Images -

- Block underneath the 12 images and search block -

To the left will be some key bullet points about the website - maybe 4 or 5 with a green tick to the left of this. Background colour will probably be best to be a light colour, possibly grey.

Then to the right of this will appear 4 images, 2 before and 2 after when applying these products. Images to be used aren't fully decided on and we would like this stage of the design left to the end when the rest of the theme etc have been decided on.

Attached images are as follows :
- How the website looks as it stands
- The fold line on the website (obviously important)
- Our rough sketch of how we'd like the website homepage to look.
- We have 7 of the images ready that are all attached in this one file. Please duplicate the images on those that currently don't have the image available.

We will also be requesting a website developer to put this into action if our current designer falls through so please feel free to contact us if potentially interested.

The layout can change if you can think of something particular different / unique that works with this design. The main idea is to not only get the 12 products on view to the viewers but also the keypoints and before and after images.

Any questions, please ask away as we're bound to have forgotten a few things.

Thanks and good luck!

Hi all, keep the designs coming.

We haven't quite seen that extra special design we're after. As stated, we're after something fairly simple to suit the youth as well as the middle aged but we're also after something that bit special.

Colours to concentrate on are still and orange etc although feel free to use other colours if you have anything special in mind.

Please experience and we'll give you our honest feedback.

Many thanks all and good luck!

Hi all, this is a message to all the designers.

Some good designs coming in but we're still after that something special for the website design. Keep the designs coming and please feel free to experiment with the design colours, layout etc.

The basic principle of the website needs to remain regarding the 12 products, search within block and 4 steps all appearing on the homepage.

The 4 steps seems to work best when it's got text as well as some simple images next to this.

A variation with the product titles with how to display this, some designers have gone with a simple white background whereas others have gone with colours. Please experiment here and where possible, add a contract / texture to the colour. Please remember the product titles needs to be clear, centured and with the circle tick box to the left of it. 

We're after a fairly simple design although we need it to look 21st century, up to date as well as interesting. The key points straight away are the 4 steps as well as the 12 products so try to guide the viewer to these areas a little.

White background behind the 12 images seems to be a much, although a light colour could possibly work.

The keypoints underneath these 12 products are too very important as it outlines what we do etc. Tick colour can vary.

Next to these keypoints will be the 'before' and 'after' images, these images needs to be fairly small and ensure there is white background around the image itself.

Good luck all and any questions, feel free to ask away.

Thanks!

Hi,

 Thank you for your time and effort with these designs, we are very nearly there with the design but we've thought of something that may work for the homepage. A curved arrow from step 1 pointing to the products, this may or may not work but feel free to give it a go.

Many thanks,

Thank you to everyone for your time and efforts with the design. It's hugely appreciated so thank you all once again.

Wish you all the luck in the future.

Trade

Serif
Sans Serif

```html
<!DOCTYPE html>
<html lang="en">
<head>
<meta charset="utf-8">
<title>Wrap Finder Hub — Home</title>
<link href="https://fonts.googleapis.com/css2?family=Open+Sans:wght@400;600;700&family=Yanone+Kaffeesatz:wght@400;600;700&display=swap" rel="stylesheet">
<style>
:root{
  --orange:#e8963a;
  --orange-dark:#d9822a;
  --navy:#34497b;
  --navy-dark:#283a66;
  --dark:#2c2c2c;
  --darker:#222;
  --grey-circle:#b9b9b9;
  --white:#fff;
  --text-light:#cfcfcf;
  --card-border:#d6d6d6;
}
*{box-sizing:border-box;margin:0;padding:0}
html,body{width:851px;height:1200px;overflow:hidden;background:var(--white);font-family:"Open Sans",sans-serif}
.page{position:relative;width:851px;height:1200px}

/* header */
.site-header{position:absolute;left:0;top:0;width:851px;height:88px;background:var(--white)}
.brand{position:absolute;left:74px;top:16px;width:230px}
.brand-name{display:flex;align-items:center;gap:8px;font-family:"Yanone Kaffeesatz",sans-serif;font-weight:700;font-size:30px;color:var(--navy);line-height:1}
.brand-dot{width:26px;height:26px;border-radius:50%;background:var(--orange)}
.brand-tag{margin-top:6px;background:var(--navy);color:var(--white);font-size:9px;font-weight:700;letter-spacing:.5px;padding:2px 6px;width:228px;text-align:center}
.promo{position:absolute;left:372px;top:0;width:405px;height:88px;background:linear-gradient(180deg,#f0a443,var(--orange-dark));border-bottom-left-radius:14px;overflow:hidden}
.promo-title{position:absolute;left:42px;top:11px;font-weight:700;font-size:16px;line-height:22px;color:var(--white);letter-spacing:.3px;z-index:1}
.promo-title span{display:block;background:rgba(40,58,102,.55);padding:0 4px;margin-bottom:2px;width:fit-content}
.promo-sub{position:absolute;left:46px;top:62px;font-weight:700;font-style:italic;font-size:14px;color:var(--white);z-index:1}
.promo-map{position:absolute;left:258px;top:0;width:147px;height:88px;background:linear-gradient(90deg,rgba(217,130,42,0) 0%,#b99a52 30%,#8fa866 60%,#c9c3b4 100%)}

/* nav */
.main-nav{position:absolute;left:0;top:88px;width:851px;height:37px;background:linear-gradient(180deg,#3a3a3a,var(--darker))}
.main-nav ul{list-style:none;position:absolute;left:74px;top:0;display:flex;gap:23px;height:37px;align-items:center}
.main-nav a{color:var(--white);text-decoration:none;font-size:11px;font-weight:600}
.main-nav a.is-current{color:var(--orange)}
.site-search{position:absolute;left:581px;top:8px;width:196px;height:21px;background:#e9e9e9;border:1px solid #999}
.site-search span{position:absolute;left:6px;top:3px;font-size:10px;font-style:italic;color:#888}
.site-search svg{position:absolute;right:3px;top:2px}

/* steps */
.steps{position:absolute;left:0;top:125px;width:851px;height:200px;background:var(--orange)}
.step{position:absolute;top:31px;width:148px;height:148px;border-radius:50%;background:var(--grey-circle);border:2px solid #d2d2d2;text-align:center;color:var(--white)}
.step-num{position:absolute;left:-2px;top:-2px;width:40px;height:40px;border-radius:50%;background:var(--grey-circle);border:3px solid var(--white);font-weight:700;font-size:20px;line-height:34px}
.step-label{margin-top:40px;font-family:"Yanone Kaffeesatz",sans-serif;font-weight:600;font-size:21px;line-height:24px;text-shadow:0 1px 2px rgba(0,0,0,.35)}
.step svg{margin-top:4px}

/* products */
.products{position:absolute;left:74px;top:357px;width:705px}
.card{position:absolute;width:164px;height:155px;border:1px solid var(--card-border);background:var(--white)}
.card-head{position:absolute;left:-1px;top:-1px;width:164px;height:50px}
.card-head svg{position:absolute;left:0;top:0}
.card-title{position:absolute;left:0;top:8px;width:164px;text-align:center;font-family:"Yanone Kaffeesatz",sans-serif;font-size:20px;color:var(--white)}
.card-photo{position:absolute;left:26px;top:62px;width:112px;height:80px;border-radius:6px}

/* features */
.features{position:absolute;left:0;top:886px;width:851px;height:200px;background:var(--orange)}
.keypoints{position:absolute;left:74px;top:32px;list-style:none}
.keypoints li{font-family:"Yanone Kaffeesatz",sans-serif;font-size:19px;color:var(--white);height:36px}
.keypoints li::before{content:"›";margin-right:6px}
.showcase{position:absolute;left:317px;top:25px;width:460px;height:158px;background:var(--white);border-radius:7px}
.showcase-label{position:absolute;top:14px;font-family:"Yanone Kaffeesatz",sans-serif;font-size:19px;color:var(--navy)}
.showcase-stage{position:absolute;left:36px;top:30px;width:389px;height:104px;background:#f1f1f1}
.showcase-photo{position:absolute;top:12px;width:150px;height:80px;border-radius:6px}
.showcase-arrow{position:absolute;top:60px;font-size:32px;color:var(--dark);line-height:1}

/* footer */
.site-footer{position:absolute;left:0;top:1086px;width:851px;height:114px;background:var(--dark)}
.footer-nav{position:absolute;left:74px;top:21px;display:flex;gap:23px;list-style:none}
.footer-nav a{color:var(--text-light);text-decoration:none;font-size:11px;font-weight:600}
.copyright{position:absolute;left:74px;top:47px;font-size:10px;color:#aaa}
.newsletter-label{position:absolute;left:562px;top:25px;font-size:10px;font-weight:600;color:var(--text-light)}
.newsletter-input{position:absolute;left:562px;top:43px;width:153px;height:22px;background:#111;border:1px solid #555;font-size:10px;font-style:italic;color:#777;padding:4px}
.newsletter-btn{position:absolute;left:715px;top:43px;width:62px;height:22px;background:#3a3a3a;border:1px solid #555;color:var(--white);font-size:10px;font-weight:700;text-align:center;line-height:20px}
.social{position:absolute;left:632px;top:78px;display:flex;gap:10px}
.social span{width:21px;height:21px;border-radius:3px;display:block}
</style>
</head>
<body>
<div class="page">

<header class="site-header">
  <div class="brand">
    <div class="brand-name"><span class="brand-dot"></span>Wrap Finder Hub</div>
    <div class="brand-tag">Find and Compare Vinyl Installers</div>
  </div>
  <div class="promo">
    <div class="promo-map" role="img" aria-label="Map of UK cities under a magnifying glass"></div>
    <div class="promo-title"><span>FIND A PROFESSIONAL</span><span>VINYL INSTALLER TODAY</span></div>
    <div class="promo-sub">Search &amp; Save in Seconds!</div>
  </div>
</header>

<nav class="main-nav">
  <ul>
    <li><a href="#" class="is-current">HOME</a></li>
    <li><a href="#">ABOUT US</a></li>
    <li><a href="#">CONTACT US</a></li>
    <li><a href="#">BLOG</a></li>
    <li><a href="#">LIST YOUR</a></li>
    <li><a href="#">COMPANY HERE</a></li>
  </ul>
  <div class="site-search"><span>Search</span>
    <svg width="16" height="16" viewBox="0 0 16 16"><circle cx="6.5" cy="6.5" r="4.5" fill="none" stroke="#222" stroke-width="2"/><path d="M10 10l4.5 4.5" stroke="#222" stroke-width="2.5"/></svg>
  </div>
</nav>

<section class="steps">
  <div class="step" style="left:76px"><div class="step-num">1</div>
    <div class="step-label">Select<br>Choosen Product</div>
    <svg width="74" height="30" viewBox="0 0 74 30"><path d="M4 22c0-6 6-8 14-9l10-7h22l12 8c6 1 9 3 9 8z" fill="#fff"/><circle cx="18" cy="23" r="5" fill="#fff" stroke="#b9b9b9" stroke-width="2"/><circle cx="57" cy="23" r="5" fill="#fff" stroke="#b9b9b9" stroke-width="2"/></svg>
  </div>
  <div class="step" style="left:260px"><div class="step-num">2</div>
    <div class="step-label">Input Postcode<br>Distance + Search</div>
    <svg width="40" height="40" viewBox="0 0 40 40"><circle cx="16" cy="16" r="10" fill="none" stroke="#fff" stroke-width="5"/><path d="M23 23l12 12" stroke="#fff" stroke-width="7" stroke-linecap="round"/></svg>
  </div>
  <div class="step" style="left:445px"><div class="step-num">3</div>
    <div class="step-label">Compare<br>Companies + Prices</div>
    <svg width="40" height="40" viewBox="0 0 40 40"><path d="M20 6h12v12L16 34 4 22z" fill="#fff"/><circle cx="27" cy="11" r="2.5" fill="#b9b9b9"/></svg>
  </div>
  <div class="step" style="left:629px"><div class="step-num">4</div>
    <div class="step-label">Contact<br>Choosen Company</div>
    <svg width="40" height="40" viewBox="0 0 40 40"><circle cx="20" cy="20" r="17" fill="none" stroke="#fff" stroke-width="3"/><path d="M14 11c-3 3-2 9 3 14s11 6 13 3l-4-4-3 2c-2-1-5-4-6-6l2-3z" fill="#fff"/></svg>
  </div>
</section>

<main class="products">
  <article class="card" style="left:0;top:0"><div class="card-head"><svg width="164" height="50"><path d="M0 0H164V40C120 30 44 30 0 40Z" fill="var(--navy)"/></svg><div class="card-title">Colour Change Wrap</div></div><div class="card-photo" role="img" aria-label="White van with colour change wrap" style="background:linear-gradient(#f4f4f4,#cfcfcf)"></div></article>
  <article class="card" style="left:180px;top:0"><div class="card-head"><svg width="164" height="50"><path d="M0 0H164V40C120 30 44 30 0 40Z" fill="var(--navy)"/></svg><div class="card-title">Printed Vehicle Wrap</div></div><div class="card-photo" role="img" aria-label="Van with printed green and sky wrap" style="background:linear-gradient(#8fb4d8,#5f9a45)"></div></article>
  <article class="card" style="left:360px;top:0"><div class="card-head"><svg width="164" height="50"><path d="M0 0H164V40C120 30 44 30 0 40Z" fill="var(--navy)"/></svg><div class="card-title">Window Tint</div></div><div class="card-photo" role="img" aria-label="Two green cars with tinted windows" style="background:linear-gradient(#6fcf5a,#2f8e2a)"></div></article>
  <article class="card" style="left:540px;top:0"><div class="card-head"><svg width="164" height="50"><path d="M0 0H164V40C120 30 44 30 0 40Z" fill="var(--navy)"/></svg><div class="card-title">Headlight Tint</div></div><div class="card-photo" role="img" aria-label="Dark car front with tinted headlights" style="background:linear-gradient(#777,#2b2b2b)"></div></article>

  <article class="card" style="left:0;top:176px"><div class="card-head"><svg width="164" height="50"><path d="M0 0H164V40C120 30 44 30 0 40Z" fill="var(--navy)"/></svg><div class="card-title">Vehicle Signage</div></div><div class="card-photo" role="img" aria-label="Van with green signage graphics" style="background:linear-gradient(90deg,#333,#b7cf3c,#eee)"></div></article>
  <article class="card" style="left:180px;top:176px"><div class="card-head"><svg width="164" height="50"><path d="M0 0H164V40C120 30 44 30 0 40Z" fill="var(--navy)"/></svg><div class="card-title">Shop Signage</div></div><div class="card-photo" role="img" aria-label="Shop front with sign board" style="background:linear-gradient(#e8e8e8,#3a3a3a 40%,#e8e8e8)"></div></article>
  <article class="card" style="left:360px;top:176px"><div class="card-head"><svg width="164" height="50"><path d="M0 0H164V40C120 30 44 30 0 40Z" fill="var(--navy)"/></svg><div class="card-title">Roof Vinyl Wrap</div></div><div class="card-photo" role="img" aria-label="Silver car with black roof wrap" style="background:linear-gradient(135deg,#333,#c8c8c8)"></div></article>
  <article class="card" style="left:540px;top:176px"><div class="card-head"><svg width="164" height="50"><path d="M0 0H164V40C120 30 44 30 0 40Z" fill="var(--navy)"/></svg><div class="card-title">Bonnet Winyl Wrap</div></div><div class="card-photo" role="img" aria-label="Silver car with black bonnet wrap" style="background:linear-gradient(135deg,#c8c8c8,#333)"></div></article>

  <article class="card" style="left:0;top:355px"><div class="card-head"><svg width="164" height="50"><path d="M0 0H164V40C120 30 44 30 0 40Z" fill="var(--navy)"/></svg><div class="card-title">Carbon Fibre Vinyl</div></div><div class="card-photo" role="img" aria-label="Silver hatchback with carbon fibre details" style="background:linear-gradient(#d8d8d8,#8a8a8a)"></div></article>
  <article class="card" style="left:180px;top:355px"><div class="card-head"><svg width="164" height="50"><path d="M0 0H164V40C120 30 44 30 0 40Z" fill="var(--navy)"/></svg><div class="card-title">StickerBomb Vinyl</div></div><div class="card-photo" role="img" aria-label="Car bonnet covered in sticker bomb vinyl" style="background:linear-gradient(135deg,#e9c54a,#d2534a,#4a8ad2)"></div></article>
  <article class="card" style="left:360px;top:355px"><div class="card-head"><svg width="164" height="50"><path d="M0 0H164V40C120 30 44 30 0 40Z" fill="var(--navy)"/></svg><div class="card-title">Clear Protective Vinyl</div></div><div class="card-photo" role="img" aria-label="Roll of clear protective film with squeegee" style="background:linear-gradient(#f7f7f7,#dcdcdc)"></div></article>
  <article class="card" style="left:540px;top:355px"><div class="card-head"><svg width="164" height="50"><path d="M0 0H164V40C120 30 44 30 0 40Z" fill="var(--navy)"/></svg><div class="card-title">Wheel Refurb</div></div><div class="card-photo" role="img" aria-label="Stack of refurbished alloy wheels" style="background:radial-gradient(#e0e0e0,#555)"></div></article>
</main>

<section class="features">
  <ul class="keypoints">
    <li>Compare Products, Location and Prices</li>
    <li>Installers throughout the Country</li>
    <li>Available throughout the Country</li>
    <li>Quick, Easy and Free to Search</li>
  </ul>
  <div class="showcase">
    <div class="showcase-label" style="left:110px">Before</div>
    <div class="showcase-label" style="left:291px">After</div>
    <div class="showcase-arrow" style="left:18px">‹</div>
    <div class="showcase-stage">
      <div class="showcase-photo" role="img" aria-label="White pickup truck before wrapping" style="left:14px;background:linear-gradient(#fafafa,#c4c4c4)"></div>
      <div class="showcase-photo" role="img" aria-label="Pickup truck after teal printed wrap" style="left:204px;background:linear-gradient(90deg,#4fa9b8,#2f6fa6)"></div>
    </div>
    <div class="showcase-arrow" style="left:436px">›</div>
  </div>
</section>

<footer class="site-footer">
  <ul class="footer-nav">
    <li><a href="#">ABOUT US</a></li>
    <li><a href="#">CONTACT US</a></li>
    <li><a href="#">BLOG</a></li>
    <li><a href="#">LIST YOUR COMPANY HERE</a></li>
  </ul>
  <div class="copyright">All Rights Reserved. Copyrights @ 2013</div>
  <div class="newsletter-label">Newsletter</div>
  <div class="newsletter-input">Enter your Mail ID</div>
  <div class="newsletter-btn">SUBSCRIBE</div>
  <div class="social">
    <span style="background:#3b5998"></span>
    <span style="background:#29a9e1"></span>
    <span style="background:#1f7bb6"></span>
    <span style="background:#f08a24"></span>
    <span style="background:#d34836"></span>
  </div>
</footer>

</div>
</body>
</html>
```